Bold & Power Webpage for VANTA Medical a Novel Business Solution for Clinical Labs

Informative and interactive webpage that utilizes my logo and information to draw customers into our company. The consulting company has 5 major functions.
1. Scientific Support to Clinical Sales
2. Clinical Lab Consulting
3. Develops Novel Diagnostic Test for Clinical labs
4. Process Optimization for Business
5. Physician Support for clinical results

The page should be dynamic and attractive from a marketing perspective. It should access points to upload new information in the form of publications, papers and videos. The website should have a means to be educational as well with a dynamic presentation of the information.

Target Market(s)

Medical Sales Reps
Clinical Laboratories
Medical Professionals
Scientist

Coding

Number of Pages Required

Font styles to use
Serif

Requirements
Must have
• Bold Colors, Dynamic presentation, fluid transitions, ability to request info, add PDF type information, Must professional and visually impressive
Nice to have
• Ability to upload videos, request information

```html
<!DOCTYPE html>
<html lang="en">
<head>
<meta charset="utf-8">
<title>VANTA Medical</title>
<link href="https://fonts.googleapis.com/css2?family=Raleway:wght@500;600;700;800&family=Open+Sans:wght@400;600&family=Merriweather:wght@400&display=swap" rel="stylesheet">
<style>
:root{
  --navy:#0d4a7e;
  --blue:#1e9bcb;
  --blue-dark:#1788b4;
  --ink:#2b2b2b;
  --text:#6d6d6d;
  --grey-bg:#f4f4f4;
  --footer:#2a2a2a;
  --white:#ffffff;
  --rule:#e2e2e2;
}
*{margin:0;padding:0;box-sizing:border-box}
html,body{width:677px;height:1200px;overflow:hidden;background:var(--white)}
body{position:relative;font-family:"Open Sans",Arial,sans-serif;color:var(--text)}
.abs{position:absolute}
.head{font-family:"Raleway",Arial,sans-serif}

/* nav */
.topline{left:0;top:0;width:677px;height:2px;background:var(--navy)}
.nav{left:0;top:2px;width:677px;height:62px;background:var(--white);z-index:3}
.nav a{position:absolute;top:35px;font:700 8px "Raleway",sans-serif;color:var(--ink);text-decoration:none;letter-spacing:.2px}
.nav a.active{color:var(--navy)}
.brand-plate{left:290px;top:20px;width:96px;height:64px;background:var(--white);border-radius:0 0 48px 48px;z-index:3}
.brand{left:290px;top:18px;width:96px;text-align:center;z-index:4}
.brand-dot{width:22px;height:22px;border-radius:50%;background:var(--navy);margin:0 auto 4px;border:4px solid var(--blue)}
.brand-name{font:600 17px "Merriweather",serif;color:var(--navy);letter-spacing:.5px}

/* hero */
.hero{left:0;top:64px;width:677px;height:350px;background:linear-gradient(110deg,#d9e1e7 0%,#eef2f5 38%,#c9d7e2 62%,#e6ecf0 100%)}
.hero-title{left:55px;top:176px;font:800 30px "Raleway",sans-serif;color:var(--white);letter-spacing:.3px;text-shadow:0 1px 3px rgba(0,0,0,.2)}
.hero-text{left:55px;top:210px;width:240px;font-size:7.2px;line-height:13px;color:var(--white)}
.btn{display:block;background:var(--blue);color:var(--white);font:700 7.5px "Raleway",sans-serif;text-align:center;border-radius:14px;letter-spacing:.2px}
.hero-btn{left:55px;top:243px;width:108px;height:25px;line-height:25px}
.arrow{top:190px;width:10px;height:30px}
.swoosh{left:0;top:330px;width:677px;height:90px}

/* welcome */
.welcome-title{left:0;top:407px;width:677px;text-align:center;font:700 16px "Raleway",sans-serif;color:var(--ink)}
.welcome-title span{color:var(--navy)}
.welcome-text{left:120px;top:432px;width:437px;text-align:center;font-size:7.2px;line-height:15px}
.welcome-btn{left:285px;top:483px;width:107px;height:26px;line-height:26px}

/* services */
.services{left:0;top:531px;width:677px;height:256px;background:var(--grey-bg)}
.tabs{left:56px;top:531px;width:565px;height:64px;display:flex;gap:1px}
.tab{flex:1;background:var(--blue);color:var(--white);text-align:center;font:700 7px "Raleway",sans-serif;position:relative}
.tab svg{display:block;margin:10px auto 6px;width:28px;height:28px}
.tab.current{background:var(--navy)}
.tab.current:after{content:"";position:absolute;left:50%;bottom:-6px;margin-left:-6px;border:6px solid transparent;border-bottom:0;border-top-color:var(--navy)}
.video{left:55px;top:618px;width:225px;height:142px;background:var(--white);padding:3px;box-shadow:0 0 0 1px var(--rule)}
.video-fill{width:100%;height:100%;background:linear-gradient(120deg,#4f7ea6,#8fb4cf 45%,#3f6d95)}
.play{left:150px;top:677px;width:35px;height:24px;border-radius:6px;background:#e0312b}
.play:after{content:"";position:absolute;left:14px;top:6px;border:6px solid transparent;border-right:0;border-left:9px solid var(--white)}
.support-title{left:305px;top:625px;font:700 13px "Raleway",sans-serif;color:var(--ink)}
.support-text{left:306px;top:645px;width:300px;font-size:6.9px;line-height:15.3px}
.support-btn{left:303px;top:727px;width:108px;height:25px;line-height:25px}

/* what we do / news */
.sec-title{top:805px;font:700 14.5px "Raleway",sans-serif;color:var(--ink)}
.wwd-img{left:55px;top:839px;width:213px;height:99px;background:var(--white);padding:3px;box-shadow:0 0 0 1px var(--rule)}
.wwd-fill{width:100%;height:100%;background:linear-gradient(100deg,#c88d80,#e9c6b5 40%,#b27766)}
.checks{left:56px;top:946px;width:220px;font-size:7.3px;line-height:14px;color:#555}
.checks .row{display:flex;align-items:flex-start;margin-bottom:6px}
.tick{flex:none;width:8px;height:8px;border-radius:50%;background:var(--blue);margin:3px 7px 0 0;position:relative}
.tick:after{content:"";position:absolute;left:2.5px;top:1.3px;width:2px;height:3.5px;border:solid var(--white);border-width:0 1.2px 1.2px 0;transform:rotate(45deg)}
.more{font:700 7px "Raleway",sans-serif;color:var(--blue);top:1002px}
.news{left:297px;width:324px;height:78px;border-bottom:1px solid var(--rule)}
.thumb{position:absolute;left:0;top:0;width:64px;height:56px;background:var(--white);padding:2px;box-shadow:0 0 0 1px var(--rule)}
.thumb div{width:100%;height:100%}
.news h3{position:absolute;left:79px;top:0;font:700 8px "Raleway",sans-serif;color:var(--ink)}
.news .date{position:absolute;left:79px;top:15px;font-size:6.8px;color:var(--blue);display:flex;align-items:center;gap:6px}
.news p{position:absolute;left:79px;top:29px;width:245px;font-size:6.9px;line-height:13px;white-space:normal}

/* footer */
.footer{left:0;top:1034px;width:677px;height:140px;background:var(--footer);color:var(--white)}
.foot-brand{left:55px;top:1068px;font:600 22px "Raleway",sans-serif;color:var(--white);line-height:24px}
.foot-mark{left:55px;top:1062px;width:8px;height:8px;border-radius:50%;background:var(--white)}
.foot-h{top:1057px;font:700 9px "Raleway",sans-serif;color:var(--white)}
.links{left:212px;top:1074px;font-size:6.8px;line-height:14px;list-style:none;color:#ddd}
.links li:before{content:"›";margin-right:8px;color:#aaa}
.field{left:317px;width:142px;height:23px;background:var(--white);font-size:6.3px;color:#777;padding-left:18px;line-height:23px}
.field svg{position:absolute;left:8px;top:8px}
.submit{left:316px;top:1134px;width:76px;height:21px;line-height:21px;font-size:7px}
.addr{left:506px;font-size:6.8px;line-height:11px;color:#ddd}
.addr svg{position:absolute;left:-14px;top:1px}
.bottom{left:0;top:1174px;width:677px;height:26px;background:var(--blue)}
.copy{left:55px;top:1183px;font:600 6px "Open Sans",sans-serif;color:var(--white)}
.social{left:551px;top:1180px;display:flex;gap:3px}
.social span{width:12px;height:12px;border-radius:50%;border:1px solid var(--white)}
</style>
</head>
<body>
<div class="abs topline"></div>
<nav class="abs nav">
  <a class="active" style="left:101px">HOME</a>
  <a style="left:161px">ABOUT US</a>
  <a style="left:239px">SERVICES</a>
  <a style="left:398px">WHAT WE DO</a>
  <a style="left:486px">NEWS</a>
  <a style="left:545px">CONTACT US</a>
</nav>
<div class="abs brand-plate"></div>
<div class="abs brand"><div class="brand-dot"></div><div class="brand-name">VANTA</div></div>

<section>
  <div class="abs hero" role="img" aria-label="Two lab scientists in masks and gloves working at a bench with a microscope and test tubes"></div>
  <svg class="abs arrow" style="left:16px" viewBox="0 0 10 30"><path d="M9 1 L2 15 L9 29" stroke="#fff" stroke-width="1" fill="none"/></svg>
  <svg class="abs arrow" style="left:651px" viewBox="0 0 10 30"><path d="M1 1 L8 15 L1 29" stroke="#fff" stroke-width="1" fill="none"/></svg>
  <h1 class="abs hero-title">VANTA-MEDICAL</h1>
  <p class="abs hero-text">Urine testing has been foundational in reducing liability forphysicians and ensuring patient compliance. The simplicity</p>
  <a class="abs btn hero-btn">READ MORE INFO</a>
  <svg class="abs swoosh" viewBox="0 0 677 90" preserveAspectRatio="none">
    <path d="M0 10 L677 58 L677 90 L0 90 Z" fill="#fff"/>
    <path d="M150 28 L677 52 L677 84 Z" fill="#6ab9d6"/>
    <path d="M220 30 L677 58 L677 64 Z" fill="#fff"/>
    <path d="M300 38 L677 70 L677 72 Z" fill="#fff"/>
  </svg>
</section>

<section>
  <h2 class="abs welcome-title">WELCOME TO <span>VANTA MEDICAL</span></h2>
  <p class="abs welcome-text">Urine testing has been foundational in reducing liability forphysicians and ensuring patient compliance. The simplicity of testing urine has been its greatest draw; less expertise is needed in order to implement the laboratory method, and the collection is some times seen as less invasive than blood. The simplicity of the analysis is where the advantages</p>
  <a class="abs btn welcome-btn">READ MORE INFO</a>
</section>

<section>
  <div class="abs services"></div>
  <div class="abs tabs">
    <div class="tab current"><svg viewBox="0 0 28 28" fill="none" stroke="#fff" stroke-width="1.6"><path d="M11 4h6M12 4v8L6 23h16L16 12V4"/><path d="M8 19h12" /></svg>SCIENTIFIC SUPPORT</div>
    <div class="tab"><svg viewBox="0 0 28 28" fill="#fff"><rect x="12" y="3" width="5" height="12" rx="1"/><rect x="9" y="22" width="12" height="3"/><path d="M19 10a6 6 0 0 1-2 12h-2v-2h2a4 4 0 0 0 1-8z"/></svg>CLINICAL LAB</div>
    <div class="tab"><svg viewBox="0 0 28 28"><path d="M14 24L4 13a5.5 5.5 0 0 1 10-6 5.5 5.5 0 0 1 10 6z" fill="#fff"/><path d="M6 14h5l2-4 2 7 2-3h5" stroke="#1e9bcb" stroke-width="1.3" fill="none"/></svg>DIAGNOSTIC TEST</div>
    <div class="tab"><svg viewBox="0 0 28 28" fill="none" stroke="#fff"><circle cx="14" cy="14" r="9" stroke-width="3" stroke-dasharray="3 2.6"/><circle cx="14" cy="14" r="5.5" stroke-width="1.6"/><circle cx="14" cy="14" r="2.5" fill="#fff"/></svg>PROCESS OPTIMIZATION</div>
    <div class="tab"><svg viewBox="0 0 28 28" fill="#fff"><circle cx="14" cy="9" r="5"/><path d="M5 25c0-6 4-9 9-9s9 3 9 9z"/></svg>PHYSICIAN SUPPORT</div>
  </div>
  <div class="abs video"><div class="video-fill" role="img" aria-label="Video still of two scientists handling samples with molecular diagrams overlaid"></div></div>
  <div class="abs play"></div>
  <h2 class="abs support-title">SCIENTIFIC SUPPORT TO CLINICAL SALES</h2>
  <p class="abs support-text">Small Volume Blood (SVB) for our testing platform is defined as any collection that is less than 0.5 mL of whole blood. By utilizing the latest in tandem mass spectrometry and robotic sample preparation; the total volume needed to generate accurate and reproducible results has been significantly reduced compared to traditional blood testing methodology. With our current technology, the hormone panel only requires 0.15 ml</p>
  <a class="abs btn support-btn">VIEW MORE INFO</a>
</section>

<section>
  <h2 class="abs sec-title" style="left:55px">WHAT WE DO</h2>
  <div class="abs wwd-img"><div class="wwd-fill" role="img" aria-label="Gloved hands drawing a blood sample with a syringe"></div></div>
  <div class="abs checks">
    <div class="row"><span class="tick"></span><span>Clinical Method development and validation<br>(LC-MS/MS, Immunoassay and others)</span></div>
    <div class="row"><span class="tick"></span><span style="margin-right:14px">Process Optimization</span><span class="tick"></span><span>Project Planning</span></div>
  </div>
  <a class="abs more" style="left:57px">VIEW MORE &gt;&gt;</a>

  <h2 class="abs sec-title" style="left:297px">LATEST NEWS</h2>
  <article class="abs news" style="top:838px">
    <div class="thumb"><div role="img" aria-label="Gloved hand holding a sample vial" style="background:linear-gradient(135deg,#c7c3c0,#b47c6d)"></div></div>
    <h3>APPLICATIONS TO THE CLINICAL LAB CONFERENCE</h3>
    <div class="date"><svg width="7" height="7" viewBox="0 0 7 7"><rect x=".5" y="1" width="6" height="5.5" fill="none" stroke="#1e9bcb"/><rect x=".5" y="1" width="6" height="1.6" fill="#1e9bcb"/></svg>DEC 02 2016</div>
    <p>Consulting LLC exists to empower clinical, agricultural, petroleum, and forensi laboratories through the use of technology and</p>
  </article>
  <article class="abs news" style="top:916px">
    <div class="thumb"><div role="img" aria-label="Two scientists in a laboratory" style="background:linear-gradient(135deg,#e7eef3,#9fb9cc)"></div></div>
    <h3>SMALL SAMPLE VOLUMES ARE SMALL PROBLEMS</h3>
    <div class="date"><svg width="7" height="7" viewBox="0 0 7 7"><rect x=".5" y="1" width="6" height="5.5" fill="none" stroke="#1e9bcb"/><rect x=".5" y="1" width="6" height="1.6" fill="#1e9bcb"/></svg>DEC 02 2016</div>
    <p>Consulting LLC exists to empower clinical, agricultural, petroleum, and forensic laboratories through the use of technology and</p>
  </article>
  <a class="abs more" style="left:299px">READ MORE &gt;&gt;</a>
</section>

<footer>
  <div class="abs footer"></div>
  <div class="abs foot-mark"></div>
  <div class="abs foot-brand">Brightline<br>Consulting</div>
  <h4 class="abs foot-h" style="left:212px">QUICK LINKS</h4>
  <ul class="abs links"><li>Home</li><li>About us</li><li>Services</li><li>What we do</li><li>News</li><li>Contact us</li></ul>
  <h4 class="abs foot-h" style="left:317px;top:1055px">NEWS LETTER</h4>
  <div class="abs field" style="top:1076px"><svg width="6" height="6" viewBox="0 0 6 6" fill="#777"><circle cx="3" cy="1.6" r="1.5"/><path d="M0 6c0-2 1.3-3 3-3s3 1 3 3z"/></svg>FIRST NAME</div>
  <div class="abs field" style="top:1104px"><svg width="7" height="6" viewBox="0 0 7 6" fill="#777"><rect width="7" height="5.5"/><path d="M0 0l3.5 3L7 0" stroke="#fff" fill="none" stroke-width=".8"/></svg>EMAIL ADDRESS</div>
  <a class="abs btn submit">SUBMIT</a>
  <h4 class="abs foot-h" style="left:495px">ADDRESS</h4>
  <div class="abs addr" style="top:1075px"><svg width="7" height="9" viewBox="0 0 7 9" fill="#fff"><path d="M3.5 0A3.3 3.3 0 0 0 .2 3.3C.2 5.8 3.5 9 3.5 9S6.8 5.8 6.8 3.3A3.3 3.3 0 0 0 3.5 0zm0 4.7a1.4 1.4 0 1 1 0-2.8 1.4 1.4 0 0 1 0 2.8z"/></svg>123 Street name,country name,city<br>name zip code 56465165</div>
  <div class="abs addr" style="top:1108px;font-size:7.6px;color:#fff"><svg width="8" height="8" viewBox="0 0 8 8" fill="#fff"><path d="M1.6 0l1.6 2-1 1.2a5 5 0 0 0 2.6 2.6l1.2-1L8 6.4 6.8 8C3 7.8.2 5 0 1.2z"/></svg>(555) 210-4478</div>
  <div class="abs addr" style="top:1134px;left:510px"><svg width="9" height="7" viewBox="0 0 9 7" fill="#fff" style="left:-18px"><rect width="9" height="7"/><path d="M0 0l4.5 3.5L9 0" stroke="#2a2a2a" fill="none"/></svg>hello@brightline-consult.com</div>
  <div class="abs bottom"></div>
  <div class="abs copy">COPYRIGHTS©2016VANTA.NET ALL RIGHTS RESERVED.</div>
  <div class="abs social"><span></span><span></span><span></span><span></span><span></span></div>
</footer>
</body>
</html>
```